Business Card Design for Occupational Medicine Start Up Company

We need to design a professional business card. We are a healthcare company providing occupational medicine services to blue collar industries. We are professional, efficient and high quality service providers.

Target Market(s)

Blue Collar Industry: Shipbuilding, Ports, Trucking Companies; The Executives and Safety Officers for these companies

Industry/Entity Type

Healthcare

Contact Information for Business Card

Logo, Name, Title, Email, Phone

Other font styles liked:
• Please match our Brand Guide

Requirements
Must have
• Our Company Colors and Logo

```html
<!DOCTYPE html>
<html lang="en">
<head>
<meta charset="utf-8">
<title>CrewWell Business Card</title>
<link rel="stylesheet" href="https://fonts.googleapis.com/css2?family=Arimo:wght@700&family=Montserrat:wght@400;500;700&display=swap">
<style>
  :root {
    --navy: #2d3680;
    --sky: #2ba6dc;
    --amber: #f2af51;
    --paper: #ffffff;
    --stage: #3b3b3b;
  }
  * { margin: 0; padding: 0; box-sizing: border-box; }
  html, body { width: 1200px; height: 1200px; overflow: hidden; }
  body {
    background: var(--stage);
    position: relative;
    font-family: "Montserrat", sans-serif;
  }
  .card {
    position: absolute;
    left: 180px;
    width: 839px;
    height: 480px;
    background: var(--paper);
    overflow: hidden;
  }
  .card--front { top: 61px; }
  .card--back { top: 660px; }

  .brand {
    position: absolute;
    display: flex;
    align-items: center;
    gap: 18px;
  }
  .brand__dot {
    width: 58px;
    height: 58px;
    border-radius: 50%;
    background: var(--navy);
    flex: none;
  }
  .brand__name {
    font-family: "Montserrat", sans-serif;
    font-weight: 700;
    font-size: 40px;
    letter-spacing: 1px;
    color: var(--navy);
    line-height: 1;
  }
  .card--front .brand { left: 49px; top: 68px; }

  .identity {
    position: absolute;
    right: 53px;
    top: 164px;
    text-align: right;
  }
  .identity__name {
    font-family: "Arimo", sans-serif;
    font-weight: 700;
    font-size: 42px;
    color: var(--sky);
    line-height: 1;
  }
  .identity__role {
    margin-top: 10px;
    font-weight: 500;
    font-size: 27px;
    letter-spacing: 1.5px;
    color: var(--navy);
    line-height: 1;
  }

  .contact-band {
    position: absolute;
    left: 0; top: 273px;
    width: 100%; height: 143px;
    background: var(--navy);
    color: var(--paper);
    font-size: 22px;
  }
  .contact {
    position: absolute;
    display: flex;
    align-items: center;
    line-height: 1;
  }
  .contact svg { position: absolute; fill: var(--paper); }
  .contact--phone { left: 76px; top: 40px; }
  .contact--phone svg { left: -29px; top: 1px; }
  .contact--email { left: 79px; top: 80px; }
  .contact--email svg { left: -32px; top: 6px; }
  .contact--address { left: 495px; top: 40px; line-height: 40px; margin-top: -9px; display: block; }
  .contact--address svg { left: -18px; top: 11px; }

  .stripe { position: absolute; left: 0; width: 100%; height: 24px; }
  .stripe--sky { top: 425px; background: var(--sky); }
  .stripe--amber { top: 456px; background: var(--amber); }

  .back-graphic {
    position: absolute;
    left: 0; top: 0;
    width: 560px; height: 480px;
    background: linear-gradient(120deg, var(--sky) 0%, var(--navy) 55%, var(--amber) 100%);
    clip-path: polygon(0 0, 100% 0, 62% 100%, 0 100%);
  }
  .card--back .brand {
    left: 436px;
    top: 270px;
    flex-direction: column;
    gap: 22px;
    width: 346px;
  }
  .card--back .brand__dot { width: 96px; height: 96px; }
</style>
</head>
<body>
  <section class="card card--front">
    <div class="brand">
      <span class="brand__dot"></span>
      <span class="brand__name">CREWWELL</span>
    </div>

    <div class="identity">
      <p class="identity__name">FULL NAME HERE</p>
      <p class="identity__role">Position</p>
    </div>

    <div class="contact-band">
      <p class="contact contact--phone">
        <svg width="14" height="18" viewBox="0 0 14 18"><path d="M3 1l3 4-2 2c1 3 3 5 5 6l2-2 3 3-2 3C6 17 1 10 1 3z"/></svg>
        +000-1234-5678
      </p>
      <p class="contact contact--email">
        <svg width="16" height="11" viewBox="0 0 16 11"><path d="M0 0h16v11H0z M1 1l7 5 7-5z" fill-rule="evenodd"/><path d="M1 1h14L8 6z"/></svg>
        youremail@email.com
      </p>
      <p class="contact contact--address">
        <svg width="11" height="16" viewBox="0 0 11 16"><path d="M5.5 0A5.5 5.5 0 0 0 0 5.5C0 9.5 5.5 16 5.5 16S11 9.5 11 5.5A5.5 5.5 0 0 0 5.5 0zm0 7.5a2 2 0 1 1 0-4 2 2 0 0 1 0 4z"/></svg>
        123 Main Street, 11th Floor<br>Some City
      </p>
    </div>

    <span class="stripe stripe--sky"></span>
    <span class="stripe stripe--amber"></span>
  </section>

  <section class="card card--back">
    <div class="back-graphic" role="img" aria-label="Large brand graphic in blue, navy and amber"></div>
    <div class="brand">
      <span class="brand__dot"></span>
      <span class="brand__name">CREWWELL</span>
    </div>
  </section>
</body>
</html>
```